CALM.OTTER snowsport and living

Calm Otter webpage design brief

Calm Otter is a life style brand
for those who love winter, snowboarding, and coffee.

We have log houses at some best snowboarding locations in Japan, in which easy and comfortable ambience make guests feel at home during their winter stay. Out there on the slopes, there are Calm Otter’s exclusive coffee kiosks that offer a wide selection of fine coffee from boutique roasters over the world to warm the hands and hearts of whenever our guests need!

Enjoy the snow with Calm Otter!

Tone & Manner: Simple, Tranquil, Relaxed, Enjoyable
 
Look and Feel : Monotone images of log house in the snowy winter and snowboarding people.  Capture of real-people-real-life moments. Red and blue colors can be used on icons and other vector elements in a much smaller scale in the overall picture.  Please refer to the attached color pallette.

Mainly informational with links to Stayvorn for booking
Social media registration pass over from talkloop. pagemural or Stayvorn
Recruitment link to Jobvane

Currently I do not have any pictures. So need a bit of discussion on this area.

Also the website needs to be in 3 languages, English, Chinese and Japanese.

Rough Sitemap:

Home (language selection on every page)
About
GO (snow villas)
Coffee (coffee kiosks on slopes)
Reservations

(Bottom of screen)
Contact us
Company info
Recruit

Reference website:
Quillbrook.example
Mossgate.example.jp

Attached pictures are for references not for use!!!
Color reference pls refer to attached file 4.

Reason: More updates on project briefs. Please have a look.

Target Market(s)

Snowboarders

Industry/Entity Type

Hospitality

Number of Pages Required

5+ page

Font styles to use
Sans Serif

Colors

Designer to choose colors to be used in the design.

Requirements
Must have
• Mobile version
• 3 languages
• Registration thru TalkLoop, Pagemural or Stayvorn
Nice to have
• Illustration instead of pictures

```html
<!DOCTYPE html>
<html lang="en">
<head>
<meta charset="utf-8">
<title>Calm Otter — Snowsport and Living</title>
<link rel="stylesheet" href="https://fonts.googleapis.com/css2?family=Noto+Sans+JP:wght@400;700&family=Noto+Sans+SC:wght@400;700&family=Open+Sans:ital,wght@0,300;0,400;0,600;0,700;1,400&display=swap">
<style>
:root{
  --red:#b3262d;
  --blue:#1d5fa8;
  --ink:#111;
  --text:#333;
  --muted:#777;
  --line:#999;
  --field:#e9e9e9;
  --white:#fff;
  --talk:#3dbb3d;
  --page:#1877d2;
  --job:#0a66c2;
}
*{box-sizing:border-box;margin:0;padding:0}
html,body{width:1200px;height:2786px;overflow:hidden;background:var(--white)}
body{position:relative;font-family:"Open Sans","Noto Sans JP","Noto Sans SC",Arial,sans-serif;color:var(--text)}
.abs{position:absolute}
a{color:inherit;text-decoration:none}

/* hero */
.hero{position:absolute;left:0;top:0;width:1200px;height:591px;
  background:linear-gradient(180deg,#dfe3e7 0%,#b9c1c8 35%,#8e979c 62%,#6d6a63 85%,#8a7862 100%)}
.site-header{position:absolute;left:0;top:0;width:1200px;height:70px;border-bottom:1px solid rgba(255,255,255,.55)}
.brand{position:absolute;left:100px;top:18px;font-size:24px;font-weight:300;letter-spacing:2px;color:var(--red)}
.nav{position:absolute;top:25px;font-size:14px;color:#222}
.social-job{position:absolute;left:944px;top:22px;height:22px;padding:0 5px;background:var(--job);color:var(--white);font-size:10px;font-weight:600;line-height:22px;border-radius:2px}
.flag{position:absolute;top:21px;width:36px;height:24px;overflow:hidden}
.hero-brand{position:absolute;left:253px;top:240px;font-size:24px;font-weight:300;letter-spacing:3px;color:var(--white)}
.hero-title{position:absolute;left:253px;top:272px;font-size:30px;line-height:34px;font-weight:700;color:var(--white)}
.search{position:absolute;left:243px;top:366px;width:714px;height:61px;background:var(--white);border-radius:3px;box-shadow:0 2px 6px rgba(0,0,0,.2)}
.search-hint{position:absolute;left:50px;top:20px;font-size:13px;font-weight:600;color:var(--muted)}
.search-btn{position:absolute;left:606px;top:9px;width:95px;height:41px;background:var(--red);color:var(--white);font-size:15px;font-weight:600;text-align:center;line-height:41px;border-radius:2px}
.dot{position:absolute;top:556px;width:11px;height:11px;border-radius:50%;background:#333}
.dot.on{background:#ddd}

.side-tab{position:absolute;left:1150px;width:50px;height:48px;color:var(--white);font-size:8px;font-weight:600;text-align:center;line-height:48px;border-radius:4px 0 0 4px}

/* sections */
.section-title{position:absolute;left:0;width:1200px;text-align:center;font-size:28px;font-weight:700;color:var(--ink)}
.arrow-btn{position:absolute;width:46px;height:36px;background:var(--field)}
.arrow-label{position:absolute;font-size:13px;color:#222}
.select{position:absolute;height:36px;background:var(--field);font-size:11px;color:#888;padding:10px 14px}
.select::after{content:"";position:absolute;right:14px;top:15px;border:6px solid transparent;border-top:7px solid #999}
.divider{position:absolute;left:100px;width:1000px;height:2px;background:#444}

.card{position:absolute;width:234px}
.card-photo{width:234px;height:230px}
.card-kicker{margin-top:19px;font-size:14px;font-style:italic;color:#222;padding-left:2px}
.card-name{font-size:30px;font-weight:700;color:var(--ink);line-height:38px;padding-left:2px;white-space:nowrap}
.card-price{font-size:20px;color:#222;padding-left:2px;line-height:32px}
.card-price small{font-size:13px}

.video{position:absolute;left:100px;top:1750px;width:1000px;height:467px;
  background:linear-gradient(90deg,#4a4f53 0%,#9aa3a8 28%,#e2e4e4 55%,#8c8782 80%,#3f3a36 100%)}
.play{position:absolute;left:564px;top:1936px;width:68px;height:68px;border-radius:50%;background:rgba(255,255,255,.75)}

.features{position:absolute;left:100px;top:2274px;width:1000px;height:173px;border-top:1px solid var(--line);border-bottom:1px solid var(--line)}
.feature-sep{position:absolute;top:0;width:1px;height:173px;background:var(--line)}
.feature h3{position:absolute;font-size:16px;font-weight:400;color:#222}
.feature p{position:absolute;width:204px;font-size:10.5px;line-height:14px;color:#888}
.feature .more{position:absolute;font-size:10px;color:#555}
.feature svg{position:absolute}

.footer-brand{position:absolute;left:100px;top:2494px;font-size:24px;font-weight:300;letter-spacing:2px;color:var(--red)}
.footer-about{position:absolute;left:100px;top:2538px;width:300px;font-size:12.5px;line-height:23px;color:#333}
.footer-more{position:absolute;left:100px;top:2612px;font-size:12px;color:#444}
.footer-col{position:absolute;top:2490px}
.footer-col h4{font-size:16px;font-weight:700;color:#222;margin-bottom:14px}
.footer-col li{list-style:none;font-size:13px;line-height:26px;color:#333}
.footer-col li::before{content:"›";display:inline-block;width:21px;color:#555}
.footer-rule{position:absolute;left:100px;top:2704px;width:1000px;height:1px;background:var(--line)}
.copyright{position:absolute;left:0;top:2728px;width:1200px;text-align:center;font-size:12px;color:#333}
</style>
</head>
<body>

<section class="hero" role="img" aria-label="Monotone photo of two snowboarders walking up a snowy ridge above a valley of pine trees"></section>
<header class="site-header">
  <div class="brand">CALM OTTER</div>
  <a class="nav" style="left:512px">Home</a>
  <a class="nav" style="left:572px">About</a>
  <a class="nav" style="left:634px">GO</a>
  <a class="nav" style="left:672px">Coffee</a>
  <a class="nav" style="left:738px">Reservations</a>
  <a class="nav" style="left:842px">Recruit</a>
  <a class="social-job">Jobvane</a>
  <svg class="flag" style="left:1000px" viewBox="0 0 36 24" role="img" aria-label="English"><rect width="36" height="24" fill="#2a3f8f"/><path d="M0 0L36 24M36 0L0 24" stroke="#fff" stroke-width="4"/><path d="M18 0V24M0 12H36" stroke="#fff" stroke-width="7"/><path d="M18 0V24M0 12H36" stroke="#c8202f" stroke-width="4"/></svg>
  <svg class="flag" style="left:1040px" viewBox="0 0 36 24" role="img" aria-label="Japanese"><rect width="36" height="24" fill="#fff"/><circle cx="18" cy="12" r="6.5" fill="#c8202f"/></svg>
  <svg class="flag" style="left:1080px" viewBox="0 0 36 24" role="img" aria-label="Chinese"><rect width="36" height="24" fill="#d8261c"/><polygon points="8,4 9.3,8 13.4,8 10.1,10.4 11.4,14.4 8,12 4.6,14.4 5.9,10.4 2.6,8 6.7,8" fill="#f7d21a"/></svg>
</header>

<div class="hero-brand">CALM OTTER</div>
<h1 class="hero-title">Log houses on the best slopes,<br>and good coffee on every run.</h1>
<div class="search">
  <svg class="abs" style="left:20px;top:22px" width="17" height="17" viewBox="0 0 17 17"><circle cx="7" cy="7" r="5.5" fill="none" stroke="#777" stroke-width="2"/><path d="M11 11L16 16" stroke="#777" stroke-width="2"/></svg>
  <span class="search-hint">Try to find your snow villa</span>
  <a class="search-btn">Search</a>
</div>
<span class="dot" style="left:551px"></span>
<span class="dot" style="left:576px"></span>
<span class="dot on" style="left:601px"></span>
<span class="dot" style="left:626px"></span>

<a class="side-tab" style="top:98px;background:var(--talk)">TalkLoop</a>
<a class="side-tab" style="top:156px;background:var(--page)">Pagemural</a>

<!-- Snow villas -->
<h2 class="section-title" style="top:615px">GO — Snow Villas</h2>
<div class="arrow-btn" style="left:100px;top:674px"><svg width="46" height="36" viewBox="0 0 46 36"><path d="M31 18H15M20 13L15 18L20 23" fill="none" stroke="#111" stroke-width="2.5"/></svg></div>
<span class="arrow-label" style="left:156px;top:683px">Previous</span>
<div class="select" style="left:320px;top:674px;width:178px">Select Resort</div>
<div class="select" style="left:511px;top:674px;width:178px">Price</div>
<div class="select" style="left:702px;top:674px;width:177px">Number of guests</div>
<span class="arrow-label" style="left:1013px;top:683px">Next</span>
<div class="arrow-btn" style="left:1053px;top:674px"><svg width="46" height="36" viewBox="0 0 46 36"><path d="M15 18H31M26 13L31 18L26 23" fill="none" stroke="#111" stroke-width="2.5"/></svg></div>

<article class="card" style="left:100px;top:751px">
  <div class="card-photo" role="img" aria-label="Log house half buried in snow among pine trees" style="background:linear-gradient(170deg,#eef0f1,#c3c7c9 55%,#6d6660)"></div>
  <p class="card-kicker">Niseko, Hokkaido</p><h3 class="card-name">Log Cabin</h3><p class="card-price">About $709 / <small>per night</small></p>
</article>
<article class="card" style="left:355px;top:751px">
  <div class="card-photo" role="img" aria-label="Warm timber living room with sofa and wood stove" style="background:linear-gradient(170deg,#e4e2df,#b3aea8 55%,#5f5954)"></div>
  <p class="card-kicker">Hakuba, Nagano</p><h3 class="card-name">Family Lodge</h3><p class="card-price">About $709 / <small>per night</small></p>
</article>
<article class="card" style="left:609px;top:751px">
  <div class="card-photo" role="img" aria-label="Loft bedroom under a wooden roof with a snowy window" style="background:linear-gradient(180deg,#a8a39e,#858280 45%,#d9dbdb)"></div>
  <p class="card-kicker">Furano, Hokkaido</p><h3 class="card-name">Studio Loft</h3><p class="card-price">About $709 / <small>per night</small></p>
</article>
<article class="card" style="left:866px;top:751px">
  <div class="card-photo" role="img" aria-label="Large log house on a ridge with snow on the roof" style="background:linear-gradient(170deg,#f2f3f4,#d5d8da 60%,#8f8f8e)"></div>
  <p class="card-kicker">Myoko, Niigata</p><h3 class="card-name">Ridge House</h3><p class="card-price">About $709 / <small>per night</small></p>
</article>

<div class="divider" style="top:1129px"></div>

<!-- Coffee kiosks -->
<h2 class="section-title" style="top:1156px">Coffee Kiosks</h2>
<div class="arrow-btn" style="left:100px;top:1216px"><svg width="46" height="36" viewBox="0 0 46 36"><path d="M31 18H15M20 13L15 18L20 23" fill="none" stroke="#111" stroke-width="2.5"/></svg></div>
<span class="arrow-label" style="left:156px;top:1225px">Previous</span>
<div class="select" style="left:416px;top:1216px;width:177px">Select Slope</div>
<div class="select" style="left:606px;top:1216px;width:178px">Roast</div>
<span class="arrow-label" style="left:1013px;top:1225px">Next</span>
<div class="arrow-btn" style="left:1053px;top:1216px"><svg width="46" height="36" viewBox="0 0 46 36"><path d="M15 18H31M26 13L31 18L26 23" fill="none" stroke="#111" stroke-width="2.5"/></svg></div>

<article class="card" style="left:100px;top:1291px">
  <div class="card-photo" role="img" aria-label="Small wooden coffee kiosk at the top of a snowy lift" style="background:linear-gradient(180deg,#c9ced3,#eef0f2 40%,#8b8e90 75%,#4d4f50)"></div>
  <p class="card-kicker">Top station</p><h3 class="card-name">Summit</h3><p class="card-price">Filter from $4</p>
</article>
<article class="card" style="left:355px;top:1291px">
  <div class="card-photo" role="img" aria-label="Snowboarder holding a steaming paper cup in gloved hands" style="background:linear-gradient(180deg,#7d848a,#b7bcc0 45%,#e3e5e6 70%,#6e6862)"></div>
  <p class="card-kicker">Mid mountain</p><h3 class="card-name">Halfway</h3><p class="card-price">Latte from $5</p>
</article>
<article class="card" style="left:609px;top:1291px">
  <div class="card-photo" role="img" aria-label="Barista pouring coffee at a kiosk counter with snow behind" style="background:linear-gradient(180deg,#b5b0aa,#8a847e 40%,#d8d9da 75%,#f2f2f2)"></div>
  <p class="card-kicker">Base lodge</p><h3 class="card-name">Powder Bar</h3><p class="card-price">Pour over from $6</p>
</article>
<article class="card" style="left:866px;top:1291px">
  <div class="card-photo" role="img" aria-label="Kiosk lit at dusk beside a tree-lined run" style="background:linear-gradient(180deg,#9aa2aa,#c8c2ba 40%,#5e5a55 70%,#2f302f)"></div>
  <p class="card-kicker">Night run</p><h3 class="card-name">Treeline</h3><p class="card-price">Mocha from $5</p>
</article>

<div class="divider" style="top:1662px"></div>

<!-- About -->
<h2 class="section-title" style="top:1686px">About Calm Otter</h2>
<div class="video" role="img" aria-label="Video still of friends in a log house living room looking out at falling snow"></div>
<div class="play"><svg width="68" height="68" viewBox="0 0 68 68"><polygon points="27,21 48,34 27,47" fill="#222"/></svg></div>

<section class="features">
  <div class="feature-sep" style="left:340px"></div>
  <div class="feature-sep" style="left:660px"></div>
  <div class="feature">
    <svg style="left:36px;top:60px" width="40" height="40" viewBox="0 0 40 40"><circle cx="18" cy="14" r="8" fill="#222"/><path d="M4 38C4 28 10 24 18 24S32 28 32 38Z" fill="#222"/><circle cx="31" cy="31" r="7" fill="var(--red)" stroke="#fff" stroke-width="2"/></svg>
    <h3 style="left:100px;top:38px">24/7 Guest Support</h3>
    <p style="left:100px;top:64px">Our team is on call all season, in English, Chinese and Japanese.</p>
    <span class="more" style="left:100px;top:124px">Read More ›</span>
  </div>
  <div class="feature">
    <svg style="left:381px;top:58px" width="44" height="44" viewBox="0 0 44 44"><polygon points="22,2 27,7 34,6 35,13 41,17 38,23 41,29 35,32 34,39 27,38 22,43 17,38 10,39 9,32 3,29 6,23 3,17 9,13 10,6 17,7" fill="#222"/><circle cx="22" cy="22" r="11" fill="#fff"/><path d="M16 22L20 26L28 17" fill="none" stroke="var(--blue)" stroke-width="3"/></svg>
    <h3 style="left:430px;top:38px">Book via Stayvorn</h3>
    <p style="left:430px;top:64px">Every snow villa is reserved through Stayvorn with secure payment.</p>
    <span class="more" style="left:430px;top:124px">Read More ›</span>
  </div>
  <div class="feature">
    <svg style="left:710px;top:62px" width="46" height="36" viewBox="0 0 46 36"><rect x="2" y="2" width="42" height="32" fill="none" stroke="#222" stroke-width="3"/><circle cx="14" cy="14" r="4" fill="#222"/><path d="M7 27C7 21 21 21 21 27Z" fill="#222"/><path d="M26 12H38M26 18H38M26 24H38" stroke="#222" stroke-width="3"/></svg>
    <h3 style="left:762px;top:38px">Easy Sign Up</h3>
    <p style="left:762px;top:64px">Register in one step with TalkLoop, Pagemural or Stayvorn.</p>
    <span class="more" style="left:762px;top:124px">Read More ›</span>
  </div>
</section>

<footer>
  <div class="footer-brand">CALM OTTER</div>
  <p class="footer-about">Snowsport and living for those who love winter, snowboarding and coffee. Enjoy the snow with Calm Otter!</p>
  <a class="footer-more">Read More ›</a>
  <div class="footer-col" style="left:440px"><h4>Quick Links</h4><ul><li>Home</li><li>About</li><li>GO</li><li>Coffee</li><li>Reservations</li></ul></div>
  <div class="footer-col" style="left:702px"><h4>Company</h4><ul><li>Contact us</li><li>Company info</li><li>Recruit</li><li>Sign in</li><li>Login</li></ul></div>
  <div class="footer-col" style="left:951px"><h4>Languages</h4><ul><li>English</li><li>中文</li><li>日本語</li></ul></div>
  <div class="footer-rule"></div>
  <p class="copyright">© 2017 &nbsp;|&nbsp; www.calmotter.example</p>
</footer>

</body>
</html>
```